Personal Finance e-commerce website needs a simple budget design

Hello! I am starting to sell downloadable and printable budget planners, as shown in the attached file, for people to plan ahead on their personal finances. <br/><br/>I want to see a one-page design with similar columns (for example, "Expenses, Budget, and Actual"). I would also like to see the basic formula ("Net Income = Gross income - Total Expenses") somewhere on the design. Finally, I want the design to remain mostly minimalistic and simple for the average person to plan their personal monthly budgets.<br/><br/>However, other than that, the overall design, layout, and colors will be at the graphic designer's choice. If you have any questions for me, please let me know. Thank you for your time!

Industry/Entity Type

Financial Planning

Colors

Designer to choose colors to be used in the design.

Requirements
Must have
• I want to see a one-page design with similar columns (for example, "Expenses, Budget, and Actual").
• I want the design to remain mostly minimalistic and simple for the average person to plan their personal monthly budgets.
Nice to have
• I would also like to see the basic formula ("Net Income = Gross income - Total Expenses") somewhere on the design.

```html
<!DOCTYPE html>
<html lang="en">
<head>
<meta charset="utf-8">
<title>Basic Monthly Budget Planner</title>
<link href="https://fonts.googleapis.com/css2?family=Source+Sans+3:wght@400;500&display=swap" rel="stylesheet">
<style>
  :root {
    --red: #b0070b;
    --green: #7dd108;
    --navy: #3c3e78;
    --month: #bdc0d4;
    --year: #d6f1b3;
    --frame: #a9b8b8;
    --guide: #c4cccc;
    --muted: #7b7f80;
    --faint: #b5bcbd;
    --ink: #111111;
    --cyan: #c8fcfd;
  }
  * { margin: 0; padding: 0; box-sizing: border-box; }
  html, body { width: 975px; height: 1200px; overflow: hidden; }
  body { font-family: "Source Sans 3", sans-serif; color: var(--ink); }
  .sheet {
    position: relative; width: 975px; height: 1200px; overflow: hidden;
    background: linear-gradient(to bottom, #ffffff 0, #ffffff 795px, #eafdfd 800px, #e6fcfd 1065px, var(--cyan) 1070px, var(--cyan) 1200px);
  }
  .abs { position: absolute; }
  .brand { left: 62px; top: 38px; display: flex; align-items: center; gap: 8px; font-size: 22px; font-weight: 500; }
  .brand-dot { width: 18px; height: 18px; border: 1.5px solid var(--ink); border-radius: 50%; }
  .date-box { top: 4px; width: 133px; height: 48px; border-radius: 3px; }
  .date-box.month { left: 635px; background: var(--month); }
  .date-box.year { left: 777px; background: var(--year); }
  .date-label { top: 62px; width: 133px; text-align: center; font-size: 19px; }
  .title { left: 0; width: 1000px; top: 123px; text-align: center; font-size: 42px; letter-spacing: 0.5px; }
  .title .accent { color: var(--red); }
  .pill { height: 62px; border-radius: 26px; color: #fff; display: flex; align-items: center; justify-content: center; white-space: nowrap; }
  .pill.red { background: var(--red); }
  .pill.green { background: var(--green); }
  .pill.navy { background: var(--navy); }
  .col-head { top: 194px; }
  .hint { font-size: 15px; color: var(--muted); text-align: center; line-height: 18px; }
  .grid { left: 0; top: 0; }
  .formula-note { top: 1033px; height: 86px; border: 1.5px solid #cfdcdc; border-radius: 34px; background: rgba(255,255,255,0.45);
    display: flex; align-items: center; justify-content: center; text-align: center; color: var(--faint); font-size: 21px; line-height: 24px; letter-spacing: 0.8px; padding-top: 14px; }
  .formula-head { top: 978px; height: 61px; font-size: 34px; letter-spacing: 0.5px; }
  .footer { top: 1136px; left: 0; width: 975px; text-align: center; font-size: 20px; letter-spacing: 0.5px; }
</style>
</head>
<body>
<main class="sheet">
  <div class="abs brand"><span class="brand-dot"></span>Brightledger</div>

  <div class="abs date-box month"></div>
  <div class="abs date-box year"></div>
  <div class="abs date-label" style="left:635px">Month</div>
  <div class="abs date-label" style="left:777px">Year</div>

  <h1 class="abs title" style="left:-12px;font-weight:400">BASIC MONTHYL <span class="accent">BUDGET</span></h1>

  <svg class="abs grid" width="975" height="1200" viewBox="0 0 975 1200" aria-hidden="true">
    <g stroke="var(--guide)" stroke-width="1">
      <line x1="0" x2="975" y1="354" y2="354"/><line x1="0" x2="975" y1="407" y2="407"/>
      <line x1="0" x2="975" y1="461" y2="461"/><line x1="0" x2="975" y1="515" y2="515"/>
      <line x1="0" x2="975" y1="569" y2="569"/><line x1="0" x2="975" y1="623" y2="623"/>
      <line x1="0" x2="975" y1="675" y2="675"/><line x1="0" x2="975" y1="729" y2="729"/>
      <line x1="0" x2="975" y1="783" y2="783"/><line x1="0" x2="975" y1="837" y2="837"/>
      <line x1="0" x2="975" y1="890" y2="890"/><line x1="0" x2="975" y1="944" y2="944"/>
      <line x1="0" x2="975" y1="1066" y2="1066"/>
    </g>
    <g fill="#fff" stroke="var(--frame)" stroke-width="1.5">
      <rect x="75" y="307" width="280" height="652"/>
      <rect x="394" y="307" width="238" height="652"/>
      <rect x="664" y="307" width="239" height="652" rx="3"/>
    </g>
    <g stroke-width="1.5">
      <g stroke="var(--red)">
        <line x1="75" x2="355" y1="353" y2="353"/><line x1="75" x2="355" y1="407" y2="407"/>
        <line x1="75" x2="355" y1="460" y2="460"/><line x1="75" x2="355" y1="514" y2="514"/>
        <line x1="75" x2="355" y1="568" y2="568"/><line x1="75" x2="355" y1="622" y2="622"/>
        <line x1="75" x2="355" y1="675" y2="675"/><line x1="75" x2="355" y1="729" y2="729"/>
        <line x1="75" x2="355" y1="783" y2="783"/><line x1="75" x2="355" y1="837" y2="837"/>
        <line x1="75" x2="353" y1="890" y2="890"/><line x1="75" x2="353" y1="943" y2="943"/>
      </g>
      <g stroke="var(--green)">
        <line x1="394" x2="632" y1="353" y2="353"/><line x1="394" x2="632" y1="407" y2="407"/>
        <line x1="394" x2="632" y1="460" y2="460"/><line x1="394" x2="632" y1="514" y2="514"/>
        <line x1="394" x2="632" y1="568" y2="568"/><line x1="394" x2="632" y1="622" y2="622"/>
        <line x1="394" x2="632" y1="675" y2="675"/><line x1="394" x2="632" y1="729" y2="729"/>
        <line x1="394" x2="632" y1="783" y2="783"/><line x1="394" x2="632" y1="837" y2="837"/>
        <line x1="394" x2="632" y1="890" y2="890"/><line x1="394" x2="630" y1="943" y2="943"/>
      </g>
      <g stroke="var(--navy)">
        <line x1="664" x2="903" y1="353" y2="353"/><line x1="664" x2="903" y1="407" y2="407"/>
        <line x1="664" x2="903" y1="460" y2="460"/><line x1="664" x2="903" y1="514" y2="514"/>
        <line x1="664" x2="903" y1="568" y2="568"/><line x1="664" x2="903" y1="622" y2="622"/>
        <line x1="664" x2="903" y1="675" y2="675"/><line x1="664" x2="903" y1="729" y2="729"/>
        <line x1="664" x2="903" y1="783" y2="783"/><line x1="664" x2="903" y1="837" y2="837"/>
        <line x1="664" x2="903" y1="890" y2="890"/><line x1="664" x2="903" y1="943" y2="943"/>
      </g>
    </g>
    <g stroke-width="4">
      <line x1="311" x2="333" y1="1004" y2="1004" stroke="var(--green)"/>
      <line x1="311" x2="333" y1="1015" y2="1015" stroke="var(--green)"/>
      <line x1="600" x2="620" y1="1009" y2="1009" stroke="var(--red)"/>
    </g>
  </svg>

  <div class="abs pill red col-head" style="left:75px;width:280px;font-size:28px;letter-spacing:1px">Expenses (category)</div>
  <div class="abs pill green col-head" style="left:394px;width:238px;font-size:33px;letter-spacing:0.5px">Budget (USD)</div>
  <div class="abs pill navy col-head" style="left:664px;width:239px;font-size:33px;letter-spacing:0.5px">Actual (USD)</div>

  <p class="abs hint" style="left:75px;width:280px;top:268px">Custom category</p>
  <p class="abs hint" style="left:430px;width:160px;top:262px">What you plan to<br>spend</p>
  <p class="abs hint" style="left:712px;width:160px;top:264px">What you actually<br>spent</p>

  <div class="abs formula-note" style="left:75px;width:219px">How much money<br>you kept</div>
  <div class="abs formula-note" style="left:348px;width:238px">How much money<br>you earned</div>
  <div class="abs formula-note" style="left:635px;width:268px;padding-top:0">Actual Expenses</div>

  <div class="abs pill red formula-head" style="left:75px;width:219px">Net Income</div>
  <div class="abs pill green formula-head" style="left:348px;width:238px">Gross Income</div>
  <div class="abs pill navy formula-head" style="left:635px;width:268px">Total Expenses</div>

  <p class="abs footer">www.brightledger-plans.com</p>
</main>
</body>
</html>
```